Restaurant needs a vertical banner for fried catfish

Our restaurant is looking for an eye-catching 78.75in. x 36in. vertical physical banner ad for our fried catfish. Photos for the fried catfish will be provided as a reference but we will also accept anything similar to the photo. We will be using the following as our receptacle: https://www.plankoria.example/banner-stand/retractable-banner-stands/
The design must incorporate the following flavor texts:
Fried Catfish
Always Fresh!
Made from Scratch
Hand-cut Fillets
The Best Catfish in Texas
Served with fries, hush puppies, and a 32oz fountain drink
Also available by the pound!
The final design should be creative, professional, and eye-catching for customers.
Updates
Colors
Designer to choose colors to be used in the design.
Requirements
Must have
- We are open to any and all design elements, albeit the 'flavor texts' should not overpower, but complement the fried catfish photo. 'Fried Catfish' can be used in lieu of a main title/logo.
Nice to have
- Transparent or textured backgrounds that can encompass any or all part of the banner such as a cutting board, shadows, abstract, etc to show depth are a plus.
- Use of vectors or objects such as ribbons or shapes to encapsulate the 'flavor texts' are also encouraged.

```html
<!DOCTYPE html>
<html lang="en">
<head>
<meta charset="utf-8">
<title>Fried Catfish – Vertical Banners</title>
<link rel="stylesheet" href="https://fonts.googleapis.com/css2?family=Rammetto+One&family=Passion+One:wght@700&family=Anton&family=Roboto:ital,wght@0,500;1,500;1,700&display=swap">
<style>
  :root {
    --page-bg: #eeeff1;
    --ink: #0c0c0c;
    --white: #ffffff;

    --orange-top: #ff5600;
    --orange-bottom: #ff8c1e;
    --orange-accent: #ffe000;
    --orange-band-start: #ffab00;
    --orange-band-end: #ffd60a;
    --orange-ring: #ffc20e;

    --green-top: #c8f08e;
    --green-bottom: #c5e46c;
    --green-accent: #6b8c00;
    --green-band-start: #8cac0c;
    --green-band-end: #a4c82a;
    --green-ring: #6b8c00;

    --food-light: #f2efe8;
    --food-mid: #c98a3a;
    --food-dark: #8a4c16;
  }

  * { margin: 0; padding: 0; box-sizing: border-box; }

  html, body {
    width: 1177px;
    height: 1200px;
    overflow: hidden;
    background: var(--page-bg);
  }

  .canvas {
    position: relative;
    width: 1177px;
    height: 1200px;
  }

  .banner {
    position: absolute;
    top: 143px;
    width: 422px;
    height: 920px;
    overflow: hidden;
    background: linear-gradient(180deg, var(--bg-top), var(--bg-bottom));
    text-align: center;
  }

  .banner--orange {
    left: 113px;
    --bg-top: var(--orange-top);
    --bg-bottom: var(--orange-bottom);
    --title: var(--white);
    --accent: var(--orange-accent);
    --pill-bg: var(--white);
    --pill-text: var(--orange-top);
    --tag-bg: var(--orange-accent);
    --tag-text: var(--orange-top);
    --body-text: var(--white);
    --star: var(--white);
    --band-start: var(--orange-band-start);
    --band-end: var(--orange-band-end);
    --ring: var(--orange-ring);
  }

  .banner--green {
    left: 638px;
    --bg-top: var(--green-top);
    --bg-bottom: var(--green-bottom);
    --title: var(--ink);
    --accent: var(--green-accent);
    --pill-bg: var(--ink);
    --pill-text: var(--white);
    --tag-bg: var(--green-accent);
    --tag-text: var(--white);
    --body-text: var(--ink);
    --star: var(--green-accent);
    --band-start: var(--green-band-start);
    --band-end: var(--green-band-end);
    --ring: var(--green-ring);
  }

  .banner__top-edge {
    position: absolute;
    top: 0; left: 0;
    width: 100%;
    height: 10px;
    background: var(--ink);
  }

  .title {
    position: absolute;
    left: 0; right: 0;
    font-family: "Rammetto One", "Arial Black", sans-serif;
    color: var(--title);
    line-height: 1;
    letter-spacing: -1px;
  }
  .title--line1 { top: 30px; font-size: 66px; }
  .title--line2 { top: 100px; font-size: 66px; }

  .pill {
    position: absolute;
    left: 50%;
    transform: translateX(-50%);
    width: 183px;
    height: 31px;
    border-radius: 6px;
    font-family: "Roboto", sans-serif;
    font-weight: 500;
    font-size: 21px;
    line-height: 31px;
  }
  .pill--fresh { top: 177px; background: var(--pill-bg); color: var(--pill-text); }
  .pill--texas { top: 626px; background: var(--tag-bg); color: var(--tag-text); }

  .dish {
    position: absolute;
    left: 28px;
    top: 298px;
    width: 375px;
    height: 211px;
  }

  .headline {
    position: absolute;
    left: 0; right: 0;
    top: 576px;
    font-family: "Passion One", "Impact", sans-serif;
    font-weight: 700;
    font-size: 44px;
    line-height: 1;
    color: var(--accent);
  }

  .features {
    position: absolute;
    left: 0; right: 0;
    top: 686px;
    list-style: none;
    font-family: "Roboto", sans-serif;
    font-style: italic;
    font-weight: 500;
    font-size: 25px;
    line-height: 33px;
    color: var(--body-text);
  }
  .features__item { position: relative; }
  .features__star {
    position: absolute;
    top: 0;
    font-style: normal;
    font-size: 27px;
    color: var(--star);
  }
  .features__item--first .features__star--left { left: 34px; }
  .features__item--first .features__star--right { right: 34px; }
  .features__item--second .features__star--left { left: 53px; }
  .features__item--second .features__star--right { right: 53px; }

  .served {
    position: absolute;
    left: 0; right: 0;
    top: 759px;
    font-family: "Roboto", sans-serif;
    font-style: italic;
    font-weight: 700;
    font-size: 24px;
    line-height: 31px;
    color: var(--body-text);
  }

  .band {
    position: absolute;
    left: 0;
    top: 820px;
    width: 422px;
    height: 100px;
  }

  .by-the-pound {
    position: absolute;
    left: 0; right: 0;
    top: 866px;
    font-family: "Anton", "Impact", sans-serif;
    font-size: 32px;
    line-height: 1;
    color: var(--ink);
    letter-spacing: -0.5px;
  }
</style>
</head>
<body>
<main class="canvas">

  <section class="banner banner--orange">
    <div class="banner__top-edge"></div>
    <h1 class="title title--line1">FRIED</h1>
    <h1 class="title title--line2">CATFISH</h1>
    <p class="pill pill--fresh">Always Fresh!</p>

    <svg class="dish" viewBox="0 0 375 211" role="img" aria-label="Photo of fried catfish fillets with fries, hush puppies and a sauce cup on a white plate">
      <defs>
        <radialGradient id="dish-orange" cx="50%" cy="45%" r="55%">
          <stop offset="0" stop-color="var(--food-mid)"/>
          <stop offset="0.6" stop-color="var(--food-dark)"/>
          <stop offset="1" stop-color="var(--food-light)"/>
        </radialGradient>
      </defs>
      <ellipse cx="187.5" cy="105.5" rx="183" ry="101" fill="url(#dish-orange)" stroke="var(--ring)" stroke-width="7"/>
    </svg>

    <h2 class="headline">THE BEST CATFISH</h2>
    <p class="pill pill--texas">IN TEXAS</p>

    <ul class="features">
      <li class="features__item features__item--first"><span class="features__star features__star--left">★</span>Made from Scratch<span class="features__star features__star--right">★</span></li>
      <li class="features__item features__item--second"><span class="features__star features__star--left">★</span>Hand-cut Fillets<span class="features__star features__star--right">★</span></li>
    </ul>

    <p class="served">Served with fries, hush puppies,<br>and a 32oz fountain drink</p>

    <svg class="band" viewBox="0 0 422 100" aria-hidden="true">
      <defs>
        <linearGradient id="band-orange" x1="0" x2="1" y1="0" y2="0">
          <stop offset="0" stop-color="var(--orange-band-start)"/>
          <stop offset="1" stop-color="var(--orange-band-end)"/>
        </linearGradient>
      </defs>
      <path d="M0 7 Q211 40 422 7 L422 100 L0 100 Z" fill="url(#band-orange)"/>
      <path d="M0 5 Q211 38 422 5" fill="none" stroke="var(--ink)" stroke-width="5"/>
    </svg>
    <p class="by-the-pound">AVAILABLE BY THE POUND!</p>
  </section>

  <section class="banner banner--green">
    <div class="banner__top-edge"></div>
    <h1 class="title title--line1">FRIED</h1>
    <h1 class="title title--line2">CATFISH</h1>
    <p class="pill pill--fresh">Always Fresh!</p>

    <svg class="dish" viewBox="0 0 375 211" role="img" aria-label="Photo of fried catfish fillets with fries, hush puppies and a sauce cup on a white plate">
      <defs>
        <radialGradient id="dish-green" cx="50%" cy="45%" r="55%">
          <stop offset="0" stop-color="var(--food-mid)"/>
          <stop offset="0.6" stop-color="var(--food-dark)"/>
          <stop offset="1" stop-color="var(--food-light)"/>
        </radialGradient>
      </defs>
      <ellipse cx="187.5" cy="105.5" rx="183" ry="101" fill="url(#dish-green)" stroke="var(--ring)" stroke-width="7"/>
    </svg>

    <h2 class="headline">THE BEST CATFISH</h2>
    <p class="pill pill--texas">IN TEXAS</p>

    <ul class="features">
      <li class="features__item features__item--first"><span class="features__star features__star--left">★</span>Made from Scratch<span class="features__star features__star--right">★</span></li>
      <li class="features__item features__item--second"><span class="features__star features__star--left">★</span>Hand-cut Fillets<span class="features__star features__star--right">★</span></li>
    </ul>

    <p class="served">Served with fries, hush puppies,<br>and a 32oz fountain drink</p>

    <svg class="band" viewBox="0 0 422 100" aria-hidden="true">
      <defs>
        <linearGradient id="band-green" x1="0" x2="1" y1="0" y2="0">
          <stop offset="0" stop-color="var(--green-band-start)"/>
          <stop offset="1" stop-color="var(--green-band-end)"/>
        </linearGradient>
      </defs>
      <path d="M0 7 Q211 40 422 7 L422 100 L0 100 Z" fill="url(#band-green)"/>
      <path d="M0 5 Q211 38 422 5" fill="none" stroke="var(--ink)" stroke-width="5"/>
    </svg>
    <p class="by-the-pound">AVAILABLE BY THE POUND!</p>
  </section>

</main>
</body>
</html>
```